Provide bookkeeping and accounting services to small and growing businesses

We need website and logo design using the name Daltonby as the logo.
The target audience are small companies and startups who need:
1) Simple bookkeeping services
2) Accounting advice that only someone with many years of senior financial experience as a CPA can provide.

The services are provided by two individuals. each of whom specialize in one of the areas.

We want the website to be clean without a lot of visual distraction but don't know how to make a boring subject interesting. We believe our potential clients, small business owners, need to find what they want quickly and easily without a lot of verbiage or distractions.

We've attached a draft of the homepage and have completed the text on most of the other pages.

Target Market(s)

small and early stage growth companies in San Diego North County

Industry/Entity Type

Accounting

Number of Pages Required

1 page

Font styles to use
Sans Serif

Colors
86cfc6
33b8a4
85cae6

Requirements
Must have
• We need a design for the website homepage that includes the name Daltonby as the logo. Must include a design for the name.
• Must have color in teal or greenish blue.
Nice to have
• White background, clean, clear, uncluttered.
• We would like to use the design in a Theme on a WordPress website. Themes Maple Harbor and Copper Lantern are appealing to us.
Should not have
• Moving pictures

```html
<!DOCTYPE html>
<html lang="en">
<head>
<meta charset="utf-8">
<title>Daltonby Accounting and Bookkeeping</title>
<link rel="stylesheet" href="https://fonts.googleapis.com/css2?family=Lato:wght@400;700&family=Questrial&display=swap">
<style>
  :root {
    --teal: #33b8a4;
    --teal-soft: #4cc2ad;
    --teal-panel: #52c2b0;
    --ink: #1f1f1f;
    --body: #3b3b3b;
    --rule: #9a9a9a;
    --charcoal: #363636;
    --charcoal-deep: #2f2f2f;
    --photo-dark: #3d4650;
    --map-grey: #e2e2e2;
    --white: #ffffff;
  }
  * { margin: 0; padding: 0; box-sizing: border-box; }
  html, body { width: 1200px; height: 2190px; overflow: hidden; background: var(--white); }
  body { position: relative; font-family: "Lato", sans-serif; color: var(--body); }
  .display { font-family: "Questrial", sans-serif; font-weight: 400; }
  .abs { position: absolute; }

  /* Header */
  .top-stripe { left: 0; top: 0; width: 1200px; height: 4px; background: var(--teal); }
  .brand { left: 99px; top: 14px; }
  .brand-name { font-family: "Lato", sans-serif; font-size: 50px; line-height: 54px; color: var(--teal); font-weight: 400; }
  .brand-tag { font-size: 17px; color: var(--ink); margin-top: -2px; }
  .contact-item { top: 18px; display: flex; align-items: center; gap: 10px; font-size: 16px; color: var(--ink); }
  .contact-icon { width: 32px; height: 32px; border-radius: 50%; background: var(--teal-soft); display: flex; align-items: center; justify-content: center; }
  .main-nav { top: 64px; left: 0; width: 1200px; height: 36px; }
  .main-nav a { position: absolute; top: 0; height: 36px; line-height: 34px; font-size: 15px; color: var(--ink); text-decoration: none; transform: translateX(-50%); white-space: nowrap; }
  .main-nav a.is-active { border: 1.5px solid var(--ink); padding: 0 13px; }

  /* Hero */
  .hero { left: 0; top: 104px; width: 1200px; height: 470px; background: linear-gradient(135deg, #4b5561 0%, #38414b 55%, #2f3740 100%); }
  .hero-caption { left: 0; top: 385px; width: 1200px; height: 85px; background: rgba(30, 34, 40, 0.55); color: var(--white); text-align: center; font-size: 28px; line-height: 33px; padding-top: 9px; }
  .hero-arrow { top: 210px; }

  /* Sections */
  .section-title { left: 0; width: 1200px; text-align: center; font-size: 38px; color: var(--ink); }
  .section-title .accent { color: var(--teal); }
  .divider { left: 321px; width: 558px; height: 10px; }
  .lead { text-align: center; font-size: 15px; line-height: 23.5px; color: var(--body); }
  .btn-outline { display: flex; align-items: center; justify-content: center; border: 2px solid var(--teal); color: var(--teal); font-weight: 700; font-size: 17px; }

  /* Services */
  .service { top: 905px; width: 600px; height: 343px; text-align: center; color: var(--white); }
  .service--bookkeeping { left: 0; background: linear-gradient(135deg, #454545 0%, #383838 60%, #333 100%); }
  .service--advice { left: 600px; background: linear-gradient(135deg, #5cc6b4 0%, #4fbfac 60%, #56c4b2 100%); }
  .service-title { position: absolute; left: 0; top: 134px; width: 600px; font-size: 36px; }
  .service-text { position: absolute; left: 150px; top: 186px; width: 300px; font-size: 15px; line-height: 25px; font-weight: 700; }
  .service-btn { position: absolute; top: 247px; left: 237px; width: 172px; height: 47px; display: flex; align-items: center; justify-content: center; font-size: 17px; font-weight: 700; }
  .service--bookkeeping .service-btn { border: 2px solid var(--teal); color: var(--teal); }
  .service--advice .service-btn { left: 175px; border: 2px solid var(--charcoal-deep); color: var(--charcoal-deep); }
  .service-icon { position: absolute; top: 50px; left: 50%; transform: translateX(-50%); }

  /* Call band */
  .call-band { left: 0; top: 1571px; width: 1200px; height: 171px; background: var(--charcoal); }
  .dash { left: 0; width: 1200px; border-top: 2px dashed #bdbdbd; }
  .call-text { left: 96px; top: 49px; font-size: 28px; line-height: 41px; color: var(--white); }
  .call-btn { left: 929px; top: 61px; width: 172px; height: 48px; border: 2px solid var(--white); color: var(--white); font-weight: 700; font-size: 17px; display: flex; align-items: center; justify-content: center; }

  /* Contact */
  .map { left: 0; top: 1742px; width: 620px; height: 343px; background: linear-gradient(160deg, #e8e8e8 0%, #dcdcdc 100%); }
  .quick-contact { left: 585px; top: 1742px; width: 615px; height: 343px; background: var(--teal-panel); clip-path: polygon(15px 0, 615px 0, 615px 343px, 15px 343px, 15px 165px, 0 150px, 15px 135px); }
  .qc-title { left: 41px; top: 17px; font-size: 36px; color: var(--white); }
  .field { left: 43px; width: 445px; border: 1.5px solid rgba(255,255,255,0.85); color: var(--white); font-size: 14px; padding: 7px 14px; }
  .submit { left: 43px; top: 283px; width: 128px; height: 32px; background: var(--white); color: var(--teal); font-weight: 700; font-size: 17px; display: flex; align-items: center; justify-content: center; }

  /* Footer */
  .footer-nav { left: 0; top: 2085px; width: 1200px; height: 61px; background: var(--charcoal-deep); }
  .footer-nav a { position: absolute; top: 22px; transform: translateX(-50%); font-size: 13px; color: var(--white); text-decoration: none; text-transform: uppercase; letter-spacing: 0.3px; }
  .footer-nav a.is-active { color: var(--teal-soft); }
  .copyright { left: 0; top: 2146px; width: 1200px; height: 44px; background: var(--teal); color: var(--white); font-size: 13px; text-align: center; line-height: 44px; }
</style>
</head>
<body>

<div class="abs top-stripe"></div>

<header>
  <div class="abs brand">
    <div class="brand-name">Daltonby</div>
    <div class="brand-tag">Accounting and Bookkeeping</div>
  </div>

  <div class="abs contact-item" style="left:748px;">
    <span class="contact-icon">
      <svg width="16" height="12" viewBox="0 0 16 12"><rect x="0.5" y="0.5" width="15" height="11" fill="none" stroke="#fff" stroke-width="1.4"/><path d="M1 1 L8 7 L15 1" fill="none" stroke="#fff" stroke-width="1.4"/></svg>
    </span>
    info@daltonby.com
  </div>
  <div class="abs contact-item" style="left:949px;">
    <span class="contact-icon">
      <svg width="16" height="16" viewBox="0 0 24 24"><path fill="#fff" d="M6.6 10.8a15.1 15.1 0 0 0 6.6 6.6l2.2-2.2a1 1 0 0 1 1-.25 11.4 11.4 0 0 0 3.6.57 1 1 0 0 1 1 1V20a1 1 0 0 1-1 1A17 17 0 0 1 3 4a1 1 0 0 1 1-1h3.5a1 1 0 0 1 1 1c0 1.25.2 2.45.57 3.6a1 1 0 0 1-.25 1z"/></svg>
    </span>
    +555 010 2040
  </div>

  <nav class="abs main-nav">
    <a class="is-active" href="#" style="left:584px;">Home</a>
    <a href="#" style="left:667px;">About Us</a>
    <a href="#" style="left:758px;">Services</a>
    <a href="#" style="left:855px;">Experience</a>
    <a href="#" style="left:958px;">Resources</a>
    <a href="#" style="left:1064px;">Contact Us</a>
  </nav>
</header>

<section class="abs hero" role="img" aria-label="Photo of people working at a desk with a laptop, notebooks and financial charts">
  <svg class="abs hero-arrow" style="left:40px;" width="30" height="60" viewBox="0 0 30 60"><path d="M26 2 L4 30 L26 58" fill="none" stroke="rgba(255,255,255,0.5)" stroke-width="2"/></svg>
  <svg class="abs hero-arrow" style="left:1128px;" width="30" height="60" viewBox="0 0 30 60"><path d="M4 2 L26 30 L4 58" fill="none" stroke="rgba(255,255,255,0.8)" stroke-width="2"/></svg>
  <p class="abs hero-caption display">Providing a full range of accounting, tax, bookkeeping<br>and business consulting services</p>
</section>

<section class="about">
  <h2 class="abs section-title display" style="top:624px;">About <span class="accent">Daltonby Accounting and Bookkeeping</span></h2>
  <svg class="abs divider" style="top:682px;" viewBox="0 0 558 10"><line x1="0" y1="5" x2="272" y2="5" stroke="var(--rule)" stroke-width="1"/><circle cx="279" cy="5" r="3.5" fill="#444"/><line x1="286" y1="5" x2="558" y2="5" stroke="var(--rule)" stroke-width="1"/></svg>
  <p class="abs lead" style="left:160px; top:707px; width:880px;">Daltonby offers a flexible range of accounting and bookkeeping services and support for small and growing organizations in San Diego North County. We provide bookkeeping services specializing in LedgerLine® at your offices or remotely from ours. We also provide a broad range of accounting services or financial advice.</p>
  <a class="abs btn-outline" style="left:514px; top:796px; width:172px; height:48px;">Read More</a>
</section>

<section class="abs service service--bookkeeping">
  <svg class="service-icon" width="56" height="72" viewBox="0 0 56 72">
    <rect x="0" y="0" width="56" height="72" rx="4" fill="#fff"/>
    <rect x="7" y="7" width="42" height="14" fill="#3a3a3a"/>
    <g fill="#3a3a3a">
      <rect x="7" y="28" width="11" height="9"/><rect x="22" y="28" width="11" height="9"/><rect x="37" y="28" width="12" height="9"/>
      <rect x="7" y="41" width="11" height="9"/><rect x="22" y="41" width="11" height="9"/><rect x="37" y="41" width="12" height="22"/>
      <rect x="7" y="54" width="11" height="9"/><rect x="22" y="54" width="11" height="9"/>
    </g>
  </svg>
  <h3 class="service-title display">Simple Bookkeeping</h3>
  <p class="service-text">Lorem ipsum dolor sit amet, consectetur adipiscing elit.</p>
  <a class="service-btn">Read More</a>
</section>

<section class="abs service service--advice">
  <svg class="service-icon" width="76" height="72" viewBox="0 0 76 72">
    <circle cx="24" cy="38" r="11" fill="#fff"/>
    <path d="M4 72 C4 56 12 50 24 50 C36 50 44 56 44 72 Z" fill="#fff"/>
    <rect x="44" y="0" width="32" height="30" rx="4" fill="#fff"/>
    <path d="M50 30 L46 40 L58 30 Z" fill="#fff"/>
    <text x="60" y="24" text-anchor="middle" font-family="Lato, sans-serif" font-weight="700" font-size="24" fill="#52c2b0">$</text>
  </svg>
  <h3 class="service-title display">Accounting Advice</h3>
  <p class="service-text">Lorem ipsum dolor sit amet, consectetur adipiscing elit.</p>
  <a class="service-btn">Read More</a>
</section>

<section class="resources">
  <h2 class="abs section-title display" style="top:1297px;">Resources</h2>
  <svg class="abs divider" style="top:1347px;" viewBox="0 0 558 10"><line x1="0" y1="5" x2="272" y2="5" stroke="var(--rule)" stroke-width="1"/><circle cx="279" cy="5" r="3.5" fill="#444"/><line x1="286" y1="5" x2="558" y2="5" stroke="var(--rule)" stroke-width="1"/></svg>
  <p class="abs lead" style="left:178px; top:1372px; width:844px;">Lorem ipsum dolor sit amet, consectetur adipiscing elit. Sed vitae magna tellus. Aenean ante nunc, semper nec cursus non, rutrum ac eros. Vestibulum mattis justo ac dui bibendum consequat a ac ipsum. Praesent a arcu venenatis, auctor velit eu, suscipit libero. Quisque convallis, leo ac pharetra sagittis.</p>
  <a class="abs btn-outline" style="left:514px; top:1463px; width:172px; height:48px;">Getting Started</a>
</section>

<section class="abs call-band">
  <div class="abs dash" style="top:9px;"></div>
  <p class="abs call-text display">Lorem ipsum dolor sit amet consectetur adipiscing elit.<br>Sed vitae magna tellus aenean ante nunc.</p>
  <a class="abs call-btn">Call Us Today</a>
  <div class="abs dash" style="top:160px;"></div>
</section>

<section class="abs map" role="img" aria-label="Street map showing the office location">
  <svg class="abs" style="left:280px; top:152px;" width="30" height="42" viewBox="0 0 30 42"><path d="M15 0 C6.7 0 0 6.7 0 15 C0 26 15 42 15 42 C15 42 30 26 30 15 C30 6.7 23.3 0 15 0 Z" fill="var(--teal)"/><circle cx="15" cy="15" r="5.5" fill="#fff"/></svg>
</section>

<section class="abs quick-contact">
  <h2 class="abs qc-title display">Quick Contact</h2>
  <div class="abs field" style="top:79px; height:34px;">Name</div>
  <div class="abs field" style="top:130px; height:33px;">Email</div>
  <div class="abs field" style="top:179px; height:86px;">Message</div>
  <a class="abs submit">Submit</a>
</section>

<footer>
  <nav class="abs footer-nav">
    <a class="is-active" href="#" style="left:204px;">Home</a>
    <a href="#" style="left:340px;">About Us</a>
    <a href="#" style="left:489px;">Services</a>
    <a href="#" style="left:642px;">Experience</a>
    <a href="#" style="left:804px;">Resources</a>
    <a href="#" style="left:971px;">Contact Us</a>
  </nav>
  <p class="abs copyright">Copyright © 2016 Daltonby Accounting and Bookkeeping. All Rights Reserved.</p>
</footer>

</body>
</html>
```